tourism marketplace web app redesign*

Hi, I need our front-page redesigned. For the competition please submit a jpg of ABOVE THE FOLD ONLY. The full page redesign will be a revision request. URL is https://qp.vendomix.hu/hu/index.html login:'fullhd' and password:'asdasd' (Fold is supposed to be at "Kiemelt Ajanlatok", use all elements above that. Please use at least one extra color other than the two in the logo, or you may completely change them. FOCUS should be on the central combined search box (3 dropdown, 2 calendar picker + Kereses Button) just like lodgewave.com, staynook.com, Torvil.com, etc... The search box is always large, central, white, we want that too. We want it to look more modern, more clean AND we want to feature a changing beautiful nature photo background (like lodgewave.com).Please use our newly designed logo (in attached pdf) and use that new spelling: "fieldtrek.online"

```html
<!DOCTYPE html>
<html lang="hu">
<head>
<meta charset="utf-8">
<title>fieldtrek.online</title>
<link href="https://fonts.googleapis.com/css2?family=Ubuntu:wght@300;400;500;700&display=swap" rel="stylesheet">
<style>
:root{
  --green:#62a993;
  --green-dark:#4f9680;
  --dark:#3c3c3c;
  --darker:#333;
  --text:#444;
  --muted:#8a8a8a;
  --line:#dcdcdc;
  --light:#f4f4f4;
  --white:#fff;
  --gold:#f0b429;
}
*{box-sizing:border-box;margin:0;padding:0}
html,body{width:1200px;height:3644px;overflow:hidden}
body{font-family:'Ubuntu',sans-serif;color:var(--text);background:var(--white);position:relative}
.sec{position:absolute;left:0;width:1200px}
.center{text-align:center}
.ph{display:block}

/* top bar */
.topbar{top:0;height:24px;background:var(--white);font-size:11px;color:var(--text);display:flex;justify-content:space-between;align-items:center;padding:0 160px}
.topbar .right{display:flex;gap:18px;align-items:center}
.topbar .login{display:flex;align-items:center;gap:5px}
.topbar .login i{width:8px;height:8px;border-radius:50%;background:var(--green);display:inline-block}

/* header */
.header{top:24px;height:64px;background:var(--dark);display:flex;align-items:center;justify-content:space-between;padding:0 160px}
.brand{display:flex;align-items:center;gap:10px;color:var(--white);font-size:24px;font-weight:500}
.brand .dot{width:40px;height:40px;border-radius:50%;background:var(--green)}
.nav{display:flex;align-items:center;gap:8px;font-size:13px;color:var(--white);font-weight:500}
.nav a{padding:6px 12px;border-radius:14px}
.nav a.active{background:var(--green)}
.nav .partner{margin-left:14px;background:var(--white);color:var(--text);font-size:11px;display:flex;align-items:center;gap:6px}
.nav .partner i{width:9px;height:9px;border-radius:50%;background:var(--green);display:inline-block}

/* hero */
.hero{top:88px;height:452px;background:linear-gradient(180deg,#f3f4f1 0%,#dfe4e0 30%,#8d9a8d 55%,#4d5a48 75%,#6b5a45 100%);}
.hero h1{position:absolute;top:58px;width:100%;text-align:center;font-size:29px;font-weight:700;color:#222;letter-spacing:.5px}
.hero .sub{position:absolute;top:92px;width:100%;text-align:center;font-size:17px;color:var(--green);font-weight:500}
.search{position:absolute;left:311px;top:136px;width:576px;height:257px;background:var(--white);box-shadow:0 4px 18px rgba(0,0,0,.2)}
.tabs{display:flex;height:40px;border-bottom:1px solid var(--line)}
.tabs div{flex:1;display:flex;align-items:center;justify-content:center;font-size:14px;font-weight:700;color:#333;border-right:1px solid var(--line)}
.tabs div:last-child{border-right:0}
.tabs .on{background:var(--green);color:var(--white)}
.fields{position:absolute;left:30px;top:70px;width:516px;display:grid;grid-template-columns:1fr 1fr;gap:22px 18px}
.field{height:38px;border:1px solid var(--line);font-size:12px;color:var(--muted);display:flex;align-items:center;padding:0 12px}
.dates{display:flex;gap:8px}
.dates .field{flex:1}
.btn-search{position:absolute;left:238px;top:173px;width:100px;height:34px;border-radius:17px;background:var(--green);color:var(--white);font-size:11px;font-weight:700;display:flex;align-items:center;justify-content:center}
.stats{position:absolute;top:222px;width:100%;display:flex;justify-content:center;gap:14px;font-size:10px;color:var(--muted)}
.stats .link{color:var(--green)}

/* section titles */
.title{font-size:28px;color:#333;font-weight:400}
.title b{color:var(--green);font-weight:700}
.subtitle{font-size:12px;color:var(--muted);margin-top:6px}

/* featured */
.featured{top:540px;height:668px}
.featured .head{position:absolute;top:42px;width:100%}
.card{position:absolute;top:130px;width:430px;height:435px;background:var(--white);box-shadow:0 2px 10px rgba(0,0,0,.12)}
.card .img{height:210px}
.card .bar{height:29px;background:var(--green);color:var(--white);font-weight:700;font-size:15px;display:flex;align-items:center;justify-content:space-between;padding:0 14px}
.stars{display:flex;gap:2px}
.stars i{width:9px;height:9px;background:var(--white);clip-path:polygon(50% 0,61% 35%,98% 35%,68% 57%,79% 91%,50% 70%,21% 91%,32% 57%,2% 35%,39% 35%)}
.stars i.off{opacity:.4}
.card .body{padding:18px 16px}
.card .loc{font-size:15px;color:#333}
.card .price{font-size:19px;font-weight:700;color:#222;margin-top:4px}
.card p{font-size:11px;color:var(--muted);line-height:1.5;margin-top:12px}
.pill{display:inline-flex;align-items:center;gap:6px;height:24px;padding:0 16px;border-radius:12px;font-size:10px;font-weight:700;margin-top:14px}
.pill.fill{background:var(--green);color:var(--white)}
.pill.line{border:1px solid var(--green);color:var(--green)}
.dots{position:absolute;top:610px;width:100%;display:flex;justify-content:center;gap:6px}
.dots i{width:6px;height:6px;border-radius:3px;background:#ccc}
.dots i.on{width:14px;background:var(--green)}

/* how */
.how{top:1208px;height:232px;background:var(--dark);color:var(--white)}
.how .lead{position:absolute;left:160px;top:54px}
.how .lead h2{font-size:27px;font-weight:400;line-height:1.2}
.how .lead h2 b{color:var(--green)}
.how .lead .pill{border:1px solid #aaa;color:#ddd}
.step{position:absolute;top:40px;width:220px;text-align:center}
.step .ic{width:66px;height:66px;border-radius:50%;background:var(--green);margin:0 auto;display:flex;align-items:center;justify-content:center}
.step h3{font-size:15px;font-weight:700;margin-top:20px}
.step p{font-size:10px;color:#bbb;margin-top:10px}

/* gallery */
.gallery{top:1440px;height:540px}
.gallery .head{position:absolute;top:42px;width:100%}
.slide-side{position:absolute;top:170px;height:286px;width:60px;border-radius:6px}
.slide{position:absolute;left:309px;top:142px;width:578px;height:340px;border-radius:6px;overflow:hidden;box-shadow:0 4px 16px rgba(0,0,0,.25)}
.slide .img{position:absolute;inset:0}
.slide .cap{position:absolute;left:0;right:0;bottom:0;height:118px;background:rgba(40,40,40,.72);color:var(--white);padding:16px 26px}
.slide .cap h3{font-size:17px;font-weight:700}
.slide .cap p{font-size:10px;line-height:1.5;margin-top:8px;color:#ddd}
.slide .cap time{display:block;font-size:10px;font-weight:700;margin-top:8px}
.arrow{position:absolute;top:293px;width:34px;height:34px;border-radius:50%;display:flex;align-items:center;justify-content:center}
.arrow.l{left:160px;background:var(--green)}
.arrow.r{left:1006px;background:var(--darker)}

/* latest */
.latest-band{top:1980px;height:73px;background:var(--green);display:flex;align-items:center;justify-content:space-between;padding:0 160px;color:var(--white)}
.latest-band h2{font-size:28px;font-weight:400}
.latest-band h2 b{font-weight:700}
.pill.ghost{border:1px solid var(--white);color:var(--white);margin-top:0}
.latest{top:2053px;height:224px;display:flex}
.tile{width:300px;height:224px;position:relative}
.tile .meta{position:absolute;left:12px;right:12px;bottom:12px;display:flex;justify-content:space-between;align-items:center;color:var(--white);font-size:13px;font-weight:700}
.tile .count{display:flex;align-items:center;gap:6px;border:1px solid rgba(255,255,255,.8);border-radius:12px;padding:3px 10px;font-weight:400}

/* newsletter */
.news{top:2277px;height:263px}
.news h2{position:absolute;top:50px;width:100%;display:flex;justify-content:center;align-items:center;gap:10px;font-size:28px;font-weight:700;color:#333}
.news .subtitle{position:absolute;top:92px;width:100%}
.news .form{position:absolute;left:389px;top:150px;width:425px;height:30px;display:flex}
.news .form .in{flex:1;border:1px solid var(--line);border-radius:15px 0 0 15px;font-size:11px;color:var(--muted);padding:0 14px;display:flex;align-items:center}
.news .form .go{width:100px;background:var(--darker);color:var(--white);border-radius:0 15px 15px 0;font-size:11px;display:flex;align-items:center;justify-content:center}
.news .note{position:absolute;top:203px;width:100%;font-size:11px;color:var(--muted)}
.news .note span{color:var(--green)}

/* testimonials */
.testi{top:2540px;height:430px;background:var(--green);color:var(--white)}
.testi .head{position:absolute;top:40px;width:100%}
.testi .title{color:var(--white)}
.testi .title b{color:var(--white)}
.testi .subtitle{color:#e3f1ec}
.quote{position:absolute;left:236px;top:121px;width:728px;height:170px;background:var(--white);border-radius:6px;color:var(--text);text-align:center;padding:22px 60px}
.quote .mark{font-size:30px;font-weight:700;color:var(--green);line-height:1}
.quote p{font-size:11px;color:var(--muted);line-height:1.55;margin-top:6px}
.quote h4{font-size:13px;color:var(--green);margin-top:14px}
.quote small{font-size:10px;color:var(--muted)}
.quote::after{content:"";position:absolute;left:354px;bottom:-10px;border:10px solid transparent;border-bottom:0;border-top-color:var(--white)}
.avatars{position:absolute;top:322px;width:100%;display:flex;justify-content:center;align-items:center;gap:12px}
.av{width:48px;height:48px;border-radius:50%;background:#8cc0af;border:2px solid #a9d1c4}
.av.on{width:56px;height:56px;background:#d9e8e3;border-color:var(--white)}
.nav-dot{width:24px;height:24px;border-radius:50%;display:flex;align-items:center;justify-content:center}
.nav-dot.l{background:#8cc0af}
.nav-dot.r{background:var(--white)}

/* stories */
.stories{top:2970px;height:342px}
.stories .head{position:absolute;left:160px;top:48px}
.stories .more{position:absolute;right:160px;top:56px;margin-top:0}
.story{position:absolute;top:109px;height:177px;box-shadow:0 2px 8px rgba(0,0,0,.1);background:var(--white)}
.story .img{height:150px}
.story .cap{height:27px;font-size:14px;font-weight:700;display:flex;align-items:center;padding:0 10px;color:#333}
.story .cap.on{background:var(--green);color:var(--white)}

/* footer */
.footer{top:3312px;height:308px;background:var(--dark);color:#ccc}
.footer .about{position:absolute;left:160px;top:48px;width:270px}
.footer .about .brand{font-size:22px}
.footer .about p{font-size:11px;line-height:1.6;margin-top:16px;color:#bbb}
.contact{margin-top:16px;font-size:11px;color:var(--white)}
.contact div{display:flex;align-items:center;gap:8px;margin-top:6px}
.col{position:absolute;top:52px}
.col h4{font-size:14px;color:var(--white);font-weight:700;margin-bottom:14px}
.col li{list-style:none;font-size:11px;margin-bottom:18px;color:#bbb}
.col li.on{color:var(--green)}
.social{display:flex;flex-direction:column;gap:16px}
.social i{width:18px;height:18px;background:#bbb;border-radius:2px;display:block}
.bottombar{top:3620px;height:24px;background:var(--white);font-size:10px;color:var(--muted);display:flex;align-items:center;padding:0 160px}
.bottombar span{color:var(--green)}
</style>
</head>
<body>

<div class="sec topbar">
  <div>Magyar ▾</div>
  <div class="right"><span>EUR ▾</span><span class="login"><i></i>Bejelentkezés | Regisztráció</span></div>
</div>

<header class="sec header">
  <div class="brand"><span class="dot"></span>fieldtrek.online</div>
  <nav class="nav">
    <a class="active">Országok</a><a>Vadfajok</a><a>Rólunk</a><a>ÁSZF</a><a>Hogyan működik</a>
    <a class="partner"><i></i>Légyen partnerünk</a>
  </nav>
</header>

<section class="sec hero" role="img" aria-label="Háttérfotó: ködös tóparti erdő, fenyőkkel és sziklás parttal">
  <h1>NINCS SZÜKSÉGED VADÁSZATSZERVEZŐRE!</h1>
  <div class="sub">Foglalj közvetlen a vadászterületnél</div>
  <div class="search">
    <div class="tabs"><div class="on">Egyéni vadászatok</div><div>Egyéni vadászatok</div><div>Egyéni vadászatok</div></div>
    <div class="fields">
      <div class="field">Összes vad</div>
      <div class="field">Összes ország</div>
      <div class="field">Összes ajánlat</div>
      <div class="dates"><div class="field">Augusztus 2019</div><div class="field">Augusztus 2019</div></div>
    </div>
    <div class="btn-search">KERESÉS</div>
    <div class="stats"><span>⌖ 12404 terület</span><span>⌖ 8764 ajánlat</span><span class="link">Részletes keresés</span></div>
  </div>
</section>

<section class="sec featured">
  <div class="head center"><h2 class="title">Kiemelt <b>ajánlatok</b></h2><div class="subtitle">További ajánlatok</div></div>
  <article class="card" style="left:165px">
    <div class="img ph" role="img" aria-label="Fotó: szarvasok őszi, narancssárga erdőben" style="background:linear-gradient(135deg,#e8a53a,#b4581c 60%,#6a3b1a)"></div>
    <div class="bar">Első ajánlat neve<span class="stars"><i></i><i></i><i></i><i></i><i class="off"></i></span></div>
    <div class="body">
      <div class="loc">Város neve, Hungary</div>
      <div class="price">1.234 €-tól</div>
      <p>Lorem ipsum dolor sit amet, consectetur adipiscing elit. Sed velit ipsum, volutpat eget elementum eu, aliquet at elit. Vivamus condimentum ultrices sem, ut luctus mauris tristique sed. Quisque aliquet auctor mauris nec scelerisque. Phasellus finibus tellus at massa euismod, id mattis velit tempor.</p>
      <span class="pill fill">RÉSZLETEK ›</span>
    </div>
  </article>
  <article class="card" style="left:612px">
    <div class="img ph" role="img" aria-label="Fotó: bőgő szarvas ködös, napsütötte mezőn" style="background:linear-gradient(135deg,#7f9aa6,#a08a5e 55%,#4a4a32)"></div>
    <div class="bar">Második ajánlat neve<span class="stars"><i></i><i></i><i></i><i></i><i class="off"></i></span></div>
    <div class="body">
      <div class="loc">Város neve, Hungary</div>
      <div class="price">1.234 €-tól</div>
      <p>Lorem ipsum dolor sit amet, consectetur adipiscing elit. Sed velit ipsum, volutpat eget elementum eu, aliquet at elit. Vivamus condimentum ultrices sem, ut luctus mauris tristique sed. Quisque aliquet auctor mauris nec scelerisque. Phasellus finibus tellus at massa euismod, id mattis velit tempor.</p>
      <span class="pill line">RÉSZLETEK ›</span>
    </div>
  </article>
  <div class="dots"><i class="on"></i><i></i><i></i></div>
</section>

<section class="sec how">
  <div class="lead"><h2>Hogyan<br><b>működik?</b></h2><span class="pill">RÉSZLETEK ›</span></div>
  <div class="step" style="left:376px">
    <div class="ic"><svg width="28" height="28" viewBox="0 0 28 28" fill="none" stroke="#fff" stroke-width="3"><circle cx="12" cy="12" r="8"/><path d="M18 18l7 7"/></svg></div>
    <h3>Ajánlatok keresése</h3><p>Válogasson kedvére az ajánlatok között</p>
  </div>
  <div class="step" style="left:600px">
    <div class="ic"><svg width="28" height="28" viewBox="0 0 28 28" fill="none" stroke="#fff" stroke-width="2.5"><rect x="4" y="6" width="20" height="18" rx="2"/><path d="M4 11h20M9 3v6M19 3v6"/></svg></div>
    <h3>Közvetlen foglalás</h3><p>Minden részletre kiterjedő ajánlatok</p>
  </div>
  <div class="step" style="left:823px">
    <div class="ic"><svg width="28" height="28" viewBox="0 0 28 28" fill="none" stroke="#fff" stroke-width="3.5"><path d="M6 14l6 6 11-12"/></svg></div>
    <h3>Indulhat a vadászat!</h3><p>Oké odafele hozzá!</p>
  </div>
</section>

<section class="sec gallery">
  <div class="head center"><h2 class="title">Büszkélkedj! <b>Képtár</b></h2><div class="subtitle">További képek</div></div>
  <div class="slide-side" role="img" aria-label="Előző galériakép: vadász őszi erdőben" style="left:243px;background:linear-gradient(180deg,#d49a3a,#5b4326)"></div>
  <div class="slide-side" role="img" aria-label="Következő galériakép: szarvas sötét erdőben" style="left:897px;background:linear-gradient(180deg,#6a6a62,#2f2f2a)"></div>
  <div class="slide">
    <div class="img" role="img" aria-label="Fotó: bőgő gímszarvas ködös mezőn" style="background:linear-gradient(135deg,#c9d6d8,#9aa89c 45%,#6e6a52)"></div>
    <div class="cap">
      <h3>A kép címe, vagy egyéb adat</h3>
      <p>Lorem ipsum dolor sit amet, consectetur adipiscing elit. Aenean placerat, sapien ac feugiat ultrices, turpis quam pellentesque elit, a facilisis velit risus at felis. Sed tristique semper ipsum sit amet rutrum.</p>
      <time>2018-10-12 10:00:00</time>
    </div>
  </div>
  <div class="arrow l"><svg width="12" height="12" viewBox="0 0 12 12" fill="none" stroke="#fff" stroke-width="2"><path d="M8 1L3 6l5 5"/></svg></div>
  <div class="arrow r"><svg width="12" height="12" viewBox="0 0 12 12" fill="none" stroke="#fff" stroke-width="2"><path d="M4 1l5 5-5 5"/></svg></div>
</section>

<div class="sec latest-band"><h2>Legfrissebb <b>ajánlatok</b></h2><span class="pill ghost">ÖSSZES AJÁNLAT ›</span></div>
<section class="sec latest">
  <div class="tile" role="img" aria-label="Fotó: szarvas őszi erdőben" style="background:linear-gradient(135deg,#e0a03c,#8a4a1c)"><div class="meta"><span>ORSZÁG NEVE</span><span class="count">⌖ 3320</span></div></div>
  <div class="tile" role="img" aria-label="Fotó: szarvasok tisztáson, fák alatt" style="background:linear-gradient(135deg,#5d6a3a,#a0763c)"><div class="meta"><span>ORSZÁG NEVE</span><span class="count">⌖ 1902</span></div></div>
  <div class="tile" role="img" aria-label="Fotó: szarvas zöld réten" style="background:linear-gradient(135deg,#6f9a3c,#3d5a22)"><div class="meta"><span>ORSZÁG NEVE</span><span class="count">⌖ 5469</span></div></div>
  <div class="tile" role="img" aria-label="Fotó: szarvasok narancs őszi erdőben" style="background:linear-gradient(135deg,#eaa83c,#9a4f1c)"><div class="meta"><span>ORSZÁG NEVE</span><span class="count">⌖ 2470</span></div></div>
</section>

<section class="sec news">
  <h2><svg width="30" height="22" viewBox="0 0 30 22"><rect width="30" height="22" rx="2" fill="#62a993"/><path d="M1 2l14 11L29 2" fill="none" stroke="#fff" stroke-width="2"/></svg>Hírlevél</h2>
  <div class="subtitle center">Iratkozz fel a legjobb ajánlatokért</div>
  <div class="form"><div class="in">Email cím</div><div class="go">Elküld</div></div>
  <div class="note center">A feliratkozással hozzájárulsz az adataid kezeléséhez. <span>Részletek</span></div>
</section>

<section class="sec testi">
  <div class="head center"><h2 class="title">Amit ügyfelünk <b>mondott</b></h2><div class="subtitle">Vásárlói vélemények</div></div>
  <div class="quote">
    <div class="mark">“</div>
    <p>Lorem ipsum dolor sit amet, consectetur adipiscing elit. Sed velit ipsum, volutpat eget elementum eu, aliquet at elit. Vivamus condimentum ultrices sem, ut luctus mauris tristique sed. Quisque aliquet auctor mauris nec scelerisque. Phasellus finibus tellus at massa euismod, id mattis velit tempor.</p>
    <h4>Ügyfél neve</h4><small>Város</small>
  </div>
  <div class="avatars">
    <span class="nav-dot l"><svg width="8" height="8" viewBox="0 0 8 8" fill="none" stroke="#fff" stroke-width="1.5"><path d="M5 1L2 4l3 3"/></svg></span>
    <span class="av" role="img" aria-label="Ügyfél profilkép"></span>
    <span class="av" role="img" aria-label="Ügyfél profilkép"></span>
    <span class="av on" role="img" aria-label="Kiválasztott ügyfél profilképe"></span>
    <span class="av" role="img" aria-label="Ügyfél profilkép"></span>
    <span class="av" role="img" aria-label="Ügyfél profilkép"></span>
    <span class="nav-dot r"><svg width="8" height="8" viewBox="0 0 8 8" fill="none" stroke="#62a993" stroke-width="1.5"><path d="M3 1l3 3-3 3"/></svg></span>
  </div>
</section>

<section class="sec stories">
  <div class="head"><h2 class="title">Vadász <b>történetek</b></h2></div>
  <span class="pill line more">ÖSSZES TÖRTÉNET ›</span>
  <article class="story" style="left:160px;width:277px">
    <div class="img" role="img" aria-label="Fotó: szarvas mocsaras réten" style="background:linear-gradient(135deg,#6f8aa0,#8a6a3a)"></div>
    <div class="cap on">Ez az ajánlat címe</div>
  </article>
  <article class="story" style="left:459px;width:280px">
    <div class="img" role="img" aria-label="Fotó: szarvas zöld erdei tisztáson" style="background:linear-gradient(135deg,#7ea046,#3e5a26)"></div>
    <div class="cap">Másik ajánlat címe</div>
  </article>
  <article class="story" style="left:760px;width:280px">
    <div class="img" role="img" aria-label="Fotó: szarvasok őszi erdőben" style="background:linear-gradient(135deg,#e6a23a,#934c1c)"></div>
    <div class="cap">Ez az ajánlat címe</div>
  </article>
</section>

<footer class="sec footer">
  <div class="about">
    <div class="brand"><span class="dot"></span>fieldtrek.online</div>
    <p>Neque porro quisquam est, qui dolorem ipsum quia dolor sit amet, consectetur, adipisci velit, sed quia non numquam eius modi tempora incidunt ut labore et dolore magnam aliquam quaerat.</p>
    <div class="contact">
      <div><svg width="12" height="9" viewBox="0 0 12 9"><rect width="12" height="9" fill="#ccc"/><path d="M0 0l6 5 6-5" fill="none" stroke="#3c3c3c"/></svg>info@fieldtrek.online</div>
      <div><svg width="12" height="12" viewBox="0 0 12 12"><path d="M2 1l2 0 1 3-1.5 1a7 7 0 003.5 3.5L8 7l3 1v2a1 1 0 01-1 1A9 9 0 011 2a1 1 0 011-1z" fill="#ccc"/></svg>(123) 555-0142</div>
    </div>
  </div>
  <div class="col" style="left:460px"><h4>FIELDTREK</h4><ul><li class="on">Rólunk</li><li>Menüpont</li><li>Menüpont</li><li>Menüpont</li></ul></div>
  <div class="col" style="left:686px"><h4>FEJLÉC 2</h4><ul><li>Menüpont</li><li>Menüpont</li><li>Menüpont</li><li>Menüpont</li></ul></div>
  <div class="col" style="left:836px"><h4>KÖVESS MINKET</h4><div class="social"><i></i><i></i><i></i></div></div>
</footer>

<div class="sec bottombar">Copyright ©&nbsp;<span>Fieldtrek 2019</span>&nbsp;| Privacy Policy | Terms &amp; Conditions</div>

</body>
</html>
```